Business Cards for Tax Preparation Business
KRT Tax Preparation
Business Cards for Tax Preparation Business - Financial Services
Creative Brief
Cutting-Edge
Brian K Holloway
Registered Tax Return Preparer
47 Birchmont Avenue, Suite 318 West Hartford, CT 06107
860-555-0148 x36
brian@krtfiling.example
www.krtfiling.example

```html
<!DOCTYPE html>
<html lang="en">
<head>
<meta charset="utf-8">
<title>KRT Tax Preparation – Stationery</title>
<link href="https://fonts.googleapis.com/css2?family=Open+Sans:wght@400;600;700&display=swap" rel="stylesheet">
<style>
:root{
  --navy:#1c3a8c;
  --navy-dark:#142b6b;
  --gold:#d3a43b;
  --ink:#4a4f5a;
  --muted:#8a909c;
  --paper:#ffffff;
  --ghost:#e9ecf2;
  --bg:#ffffff;
}
*{margin:0;padding:0;box-sizing:border-box}
html,body{width:1200px;height:758px;overflow:hidden;background:var(--bg);font-family:"Open Sans",Arial,sans-serif;color:var(--ink)}
.canvas{position:relative;width:1200px;height:758px}

.brand{display:flex;align-items:center;gap:6px;color:var(--navy);font-weight:700;white-space:nowrap}
.brand .mark{width:10px;height:10px;background:var(--navy)}
.brand-hero{position:absolute;left:30px;top:48px;font-size:40px;color:var(--ghost);gap:16px}
.brand-hero .mark{width:40px;height:40px;background:var(--ghost)}

/* letterhead */
.letterhead{position:absolute;left:679px;top:30px;width:444px;height:505px;background:var(--paper);box-shadow:0 1px 6px rgba(0,0,0,.18)}
.letterhead .brand{position:absolute;left:28px;top:26px;font-size:15px}
.letter-body{position:absolute;left:28px;top:78px;width:388px;font-size:6.4px;line-height:1.6}
.letter-body p{margin-bottom:8px}
.signature{width:80px;height:18px;margin:4px 0 10px;background:linear-gradient(90deg,#cfd4df,#eef0f5);border-radius:9px}
.letter-footer{position:absolute;left:0;right:0;bottom:18px;text-align:center;font-size:5.6px;color:var(--muted)}
.letter-band{position:absolute;left:0;right:0;bottom:0;height:6px;background:var(--navy);border-top:2px solid var(--gold)}

/* envelope */
.envelope{position:absolute;left:115px;top:329px;width:538px;height:204px}
.envelope svg{position:absolute;left:0;top:0}
.envelope-body{position:absolute;left:0;top:54px;width:538px;height:150px;background:var(--paper);box-shadow:0 1px 6px rgba(0,0,0,.18)}
.envelope-body .brand{position:absolute;left:20px;top:14px;font-size:14px}
.envelope-return{position:absolute;left:20px;bottom:16px;font-size:5.6px;line-height:1.6;color:var(--muted);width:260px}
.envelope-flap-name{position:absolute;left:0;right:0;top:28px;text-align:center;font-size:7px;font-weight:700;color:#fff}
.envelope-band{position:absolute;left:0;right:0;bottom:0;height:5px;background:var(--navy)}

/* cards */
.card{position:absolute;top:554px;width:254px;height:166px;background:var(--paper);box-shadow:0 1px 5px rgba(0,0,0,.2);overflow:hidden}
.card .brand{position:absolute;left:14px;top:16px;font-size:11px}
.card .person{position:absolute;font-size:10px;font-weight:700;color:var(--navy);white-space:nowrap}
.card .role{display:block;font-size:5.5px;font-weight:400;color:var(--muted);margin-top:1px}
.card .contact{position:absolute;font-size:5.5px;line-height:1.8;color:var(--ink);white-space:nowrap}
.card .contact span{display:inline-block;width:5px;height:5px;border-radius:50%;background:var(--navy);margin-right:4px;vertical-align:middle}
.card .address{position:absolute;font-size:5.5px;line-height:1.6;color:var(--ink);white-space:nowrap}
.card .web{position:absolute;font-size:6px;font-weight:600;color:var(--navy)}

.card-classic{left:60px}
.card-classic .person{left:14px;top:78px}
.card-classic .contact{left:14px;top:106px}
.card-classic .address{left:140px;top:78px}
.card-classic .web{left:14px;top:142px}
.card-classic .rule{position:absolute;left:0;right:0;bottom:0;height:4px;background:var(--navy)}

.card-band{left:341px}
.card-band .address{right:12px;top:42px;text-align:right}
.card-band .name-bar{position:absolute;left:0;width:190px;top:68px;height:22px;background:var(--navy)}
.card-band .person{left:14px;top:72px;color:#fff}
.card-band .role{color:var(--muted);margin-top:8px}
.card-band .contact{left:14px;top:110px}
.card-band .web{right:14px;top:136px}
.card-band .strip{position:absolute;left:0;right:0;bottom:0;height:7px;background:linear-gradient(90deg,var(--navy) 0 60%,var(--gold) 60%)}

.card-airy{left:619px}
.card-airy .address{right:12px;top:42px;text-align:right}
.card-airy .person{right:14px;top:74px;text-align:right}
.card-airy .contact{right:14px;top:102px;text-align:right}
.card-airy .web{left:14px;top:142px}
.card-airy .rule{position:absolute;left:0;right:0;bottom:0;height:2px;background:var(--navy)}

.card-footer{left:902px}
.card-footer .address{right:12px;top:42px;text-align:right}
.card-footer .person{left:14px;top:68px}
.card-footer .contact{left:14px;top:96px}
.card-footer .web{right:14px;top:130px}
.card-footer .band{position:absolute;left:0;right:0;bottom:0;height:12px;background:var(--navy);border-top:2px solid var(--gold)}
</style>
</head>
<body>
<div class="canvas">

  <div class="brand brand-hero"><i class="mark"></i>KRT Tax Preparation</div>

  <section class="envelope">
    <svg width="538" height="56" viewBox="0 0 538 56" aria-hidden="true">
      <polygon points="0,55 70,2 468,2 538,55" fill="var(--navy)"/>
      <polygon points="0,55 269,6 538,55" fill="var(--navy-dark)"/>
    </svg>
    <div class="envelope-flap-name">KRT Tax Preparation</div>
    <div class="envelope-body">
      <div class="brand"><i class="mark"></i>KRT Tax Preparation</div>
      <div class="envelope-return">47 Birchmont Avenue, Suite 318<br>Larkspur Hollow, CT 06999<br>860-555-0148 x36 · brian@krtfiling.example</div>
      <div class="envelope-band"></div>
    </div>
  </section>

  <section class="letterhead">
    <div class="brand"><i class="mark"></i>KRT Tax Preparation</div>
    <div class="letter-body">
      <p>21 May 2015</p>
      <p><strong>Dear Mr. Alan Pierce,</strong></p>
      <p>Thank you for choosing our office to prepare your annual return. We have reviewed the documents you provided and organised every form, receipt and statement so that nothing is missed when we file on your behalf this season.</p>
      <p>Please review the enclosed summary and confirm that your income, deductions and dependents are listed correctly. If anything has changed since last year, let us know before the end of the month so we can adjust your figures.</p>
      <p>Our team remains available for questions about estimated payments, refunds or state filings. We look forward to working with you again and appreciate the trust you place in our practice.</p>
      <p>Kind regards and best wishes for a smooth filing season.</p>
      <p>Your Sincerely,</p>
      <div class="signature" role="img" aria-label="Handwritten signature"></div>
    </div>
    <div class="letter-footer">47 Birchmont Avenue, Suite 318 Larkspur Hollow, CT 06999 · 860-555-0148 x36 · www.krtfiling.example</div>
    <div class="letter-band"></div>
  </section>

  <article class="card card-classic">
    <div class="brand"><i class="mark"></i>KRT Tax Preparation</div>
    <div class="person">Brian K Holloway<span class="role">Registered Tax Return Preparer</span></div>
    <div class="contact"><span></span>860-555-0148 x36<br><span></span>brian@krtfiling.example</div>
    <div class="address"><strong>KRT Tax Preparation</strong><br>47 Birchmont Avenue, Suite 318<br>Larkspur Hollow, CT 06999</div>
    <div class="web">www.krtfiling.example</div>
    <div class="rule"></div>
  </article>

  <article class="card card-band">
    <div class="brand"><i class="mark"></i>KRT Tax Preparation</div>
    <div class="address">47 Birchmont Avenue, Suite 318<br>Larkspur Hollow, CT 06999</div>
    <div class="name-bar"></div>
    <div class="person">Brian K Holloway<span class="role">Registered Tax Return Preparer</span></div>
    <div class="contact"><span></span>860-555-0148 x36<br><span></span>brian@krtfiling.example</div>
    <div class="web">www.krtfiling.example</div>
    <div class="strip"></div>
  </article>

  <article class="card card-airy">
    <div class="brand"><i class="mark"></i>KRT Tax Preparation</div>
    <div class="address">47 Birchmont Avenue, Suite 318<br>Larkspur Hollow, CT 06999</div>
    <div class="person">Brian K Holloway<span class="role">Registered Tax Return Preparer</span></div>
    <div class="contact">860-555-0148 x36<br>brian@krtfiling.example</div>
    <div class="web">www.krtfiling.example</div>
    <div class="rule"></div>
  </article>

  <article class="card card-footer">
    <div class="brand"><i class="mark"></i>KRT Tax Preparation</div>
    <div class="address">47 Birchmont Avenue, Suite 318<br>Larkspur Hollow, CT 06999</div>
    <div class="person">Brian K Holloway<span class="role">Registered Tax Return Preparer</span></div>
    <div class="contact"><span></span>860-555-0148 x36<br><span></span>brian@krtfiling.example</div>
    <div class="web">www.krtfiling.example</div>
    <div class="band"></div>
  </article>

</div>
</body>
</html>
```